Wordpress Design For Financial Investment Company

//** NEW WIREFRAME ADDED TO HELP WITH LAYOUT ISSUES. PLEASE REFER TO WIREFRAME IN ATTACHED FILES. NO DESIGN WILL BE CONSIDERED IF IT DOES NOT FOLLOW THE WIREFRAME. **//
//** PLEASE READ THE ENTIRE BRIEF INCLUDING ALL UPDATES TO THE BRIEF. THE CLIENT IS VERY SPECIFIC ABOUT WHAT THEY WANT AND I'VE COVERED SEVERAL THINGS IN THE UPDATES. THERE IS ALSO A VIDEO UPDATE THAT HAS SOME VALUABLE INFORMATION IN IT FOR THIS CONTEST. **//
The client is an investment advisor who needs a new website designed. The current site is http://www.velmorfield.net.
The client wants the site to be green to match the attached logo.
The home page should have relevant images in the rotator. No people hugging! This is a financial investment site, not a family counseling site.
Also, the client wants 4 buttons on the home page to highlight the 4 main areas they focus on:
Investment Advice and Education
General Financial Planning
Retirement Planning
401K Planning
The top right area of the site needs to have their phone number, a call to action, and 2 buttons.
Their phone number is 303-418-7639
The call to action should say something like "Call for a free consultation!"
The buttons need to say:
Login To Your Bluvexa Account
Login To Your Quillbrook Account
The final design should communicate professionalism, financial safety and growth.
Main navigation should be:
Home
About Us
Associates
Services
Contact
Mission Statement (Could also be "Our Mission")
This is a site that the client likes: http://www.pwkinvestmentconsulting.com/
Updates
The designs should not have:
Newsletter content. A newsletter sign up is fine
Learning Center
Calculators
Stock prices/tickers
The design should have a contact form on the page.
I have talked to my client and have some updates. I did a video update because I thought it would be easier to show what I'm trying to get across.
Reason: I am going to be extending the contest a few more days. I'm still not getting quite what I want and very few people are even trying to follow the creative brief and the updates to it.
PLEASE read the entire brief and the updates. There is also a video I made that explains everything. I've also attached a wireframe.
Thanks!
Target Market(s)
People looking for a high-end financial investment company.
Industry/Entity Type
Investment
Requirements
Must have
- !!FOLLOW THE WIREFRAME FOR LAYOUT!!
!!THEIR LOGO!!
4 buttons to highlight their main practice areas
Phone number in the top right
"Free Consultation" call to action
2 Login buttons in the top right
A contact form on the page.
Should not have
- The designs should not have:
Learning Center
Calculators
Stock prices/tickers

```html
<!DOCTYPE html>
<html lang="en">
<head>
<meta charset="utf-8">
<title>Velmorfield Financial</title>
<link rel="stylesheet" href="https://fonts.googleapis.com/css2?family=Arimo:wght@400;700&family=Tinos:ital@1&display=swap">
<style>
:root{
  --green-deep:#1f3a29;
  --green:#27452f;
  --green-band:#3d5e48;
  --green-light:#5f9a6e;
  --cream:#f3e6d3;
  --cream-panel:#f8ecdc;
  --cream-field:#fdf6ea;
  --line:#c9b79b;
  --text:#3a3a32;
  --link:#7fb98b;
  --footer:#1d3125;
  --footer-bottom:#15241b;
}
*{box-sizing:border-box;margin:0;padding:0}
html,body{width:690px;height:1200px;overflow:hidden}
body{position:relative;background:var(--cream);font-family:"Arimo",Arial,sans-serif;color:var(--text);font-size:7px;line-height:1.45}
.abs{position:absolute}
.top{left:0;top:0;width:690px;height:268px;background:var(--green-deep)}
.nav-band{left:0;top:56px;width:690px;height:37px;background:linear-gradient(90deg,#35553f,#4a6c55 30%,#3b5b46 60%,#4c6e57);border-top:1px solid #5a7a63;border-bottom:1px solid #14281b}
.nav a{position:absolute;top:13px;color:#e8e0cf;text-decoration:none;font-size:8px}
.nav .active{left:8px;top:3px;width:71px;height:30px;background:#1a2a20;color:#fff;text-align:center;line-height:30px}
.login{top:19px;height:20px;border:1px solid #b5a98c;background:var(--green);color:#f3ead8;font-size:6px;line-height:7px;text-align:center;padding:3px 3px 0 18px;border-radius:2px}
.login svg{position:absolute;left:5px;top:5px}
.logo{left:285px;top:34px;width:101px;height:72px;border-radius:50%;background:var(--cream);border:3px solid #3a2a20;text-align:center;color:#3a2a20;font-weight:700;font-size:10px;line-height:12px;padding-top:22px}
.ribbon{left:213px;top:102px;width:250px;height:24px}
.ribbon span{position:absolute;left:0;top:0;width:250px;text-align:center;line-height:24px;font-family:"Tinos",serif;font-style:italic;font-size:7px;color:#2a2a22}
.call{left:490px;top:106px;color:#fff;font-size:9px;line-height:14px}
.call svg{vertical-align:middle;margin-right:4px}
.slider{left:8px;top:138px;width:668px;height:192px;background:var(--cream-panel);border:1px solid #d8c6a8;border-radius:3px;box-shadow:0 1px 3px rgba(0,0,0,.3)}
.slide-img{left:8px;top:7px;width:436px;height:176px;background:linear-gradient(180deg,#4e86c6 0%,#a9cbe8 45%,#d9b27a 62%,#c8985a 100%)}
.slide-title{left:472px;top:5px;font-size:16px;color:var(--green);letter-spacing:.5px}
.slide-text{left:472px;top:44px;width:188px;text-align:justify;font-size:6.6px;line-height:9.5px}
.btn-light{border:1px solid #a99a80;background:var(--cream-field);color:var(--text);font-weight:700;font-size:7px;text-align:center;border-radius:2px}
.btn-dark{background:var(--green);color:#fff;font-weight:700;font-size:7px;text-align:center;border-radius:2px}
.dots{left:610px;top:176px}
.dots i{display:inline-block;width:10px;height:10px;border-radius:50%;background:#c9c0b2;margin-right:3px}
.dots i:first-child{background:var(--green)}
.card{width:197px;height:158px;background:var(--cream-panel);border:1px solid #d7c4a6;border-radius:2px}
.card h3{height:16px;background:var(--green);color:#fff;font-weight:400;font-size:9px;text-align:center;line-height:16px;letter-spacing:.3px}
.card .photo{position:absolute;left:6px;top:26px;width:184px;height:59px;border-radius:3px}
.card p{position:absolute;left:5px;top:92px;width:186px;height:37px;overflow:hidden;text-align:justify;font-size:6.6px;line-height:9.2px}
.card .more{position:absolute;left:68px;top:150px;width:62px;height:13px;line-height:13px}
.panel{background:var(--cream-panel);border:1px solid #e2d2b8;border-radius:2px}
.panel h4{position:absolute;font-weight:400;font-size:9px;color:var(--green);letter-spacing:.5px}
.label{position:absolute;left:15px;font-size:6px}
.field{position:absolute;left:78px;width:147px;height:15px;background:var(--cream-field);border:1px solid var(--green)}
.sep{left:0;top:739px;width:690px;border-top:1px dashed #8d9a86}
.sec-title{top:762px;font-size:9px;color:var(--green);letter-spacing:.3px}
.date{left:8px;width:39px;height:27px;background:var(--green);color:#fff;text-align:center;border-radius:2px}
.date b{display:block;font-size:12px;line-height:14px;padding-top:1px}
.date span{display:block;font-size:6px;line-height:8px}
.blurb{font-size:6.6px;line-height:9.2px;text-align:justify}
.rm{font-style:italic;text-decoration:underline;font-size:6.4px}
.vdiv{top:785px;height:183px;border-left:1px dotted #6f6f60}
.hdiv{left:207px;width:150px;border-top:1px dotted #6f6f60}
.event-img{left:418px;width:104px;height:48px;background:linear-gradient(180deg,#e8e8e8,#9ba3aa 60%,#50555a)}
.call-strip{left:0;top:998px;width:690px;height:30px;background:#efe2cd;border-top:1px solid #d9c8ab}
.call-pill{left:268px;top:989px;width:148px;height:20px;background:var(--cream-field);border:1px solid #b9ab90;border-radius:10px;font-size:6.5px;line-height:18px;padding-left:34px}
.call-pill svg{position:absolute;left:12px;top:4px}
.footer{left:0;top:1028px;width:690px;height:147px;background:var(--footer)}
.footer h5{position:absolute;top:10px;color:#fff;font-weight:400;font-size:9px;letter-spacing:.3px}
.footer ul{position:absolute;top:31px;list-style:none;font-size:6.6px;line-height:8.8px;color:var(--link)}
.footer .info{position:absolute;color:#fff;font-size:6.5px}
.social{position:absolute;top:30px;width:30px;height:24px;border-radius:50%;background:#ddd0bb}
.brand{left:528px;top:1100px;color:#fff}
.brand i{position:absolute;left:0;top:4px;width:31px;height:20px;border-radius:50%;background:var(--cream)}
.brand b{position:absolute;left:38px;top:0;font-weight:400;font-size:17px;line-height:18px;white-space:nowrap}
.brand span{position:absolute;left:38px;top:17px;font-size:9px;white-space:nowrap}
.copy{left:0;top:1175px;width:690px;height:25px;background:var(--footer-bottom);color:#e6e6e0;text-align:center;font-size:6.5px;line-height:18px}
</style>
</head>
<body>

<header>
  <div class="abs top"></div>
  <a class="abs login" style="left:492px;width:88px">Login for your<br>Bluvexa account
    <svg width="8" height="9" viewBox="0 0 8 9"><rect x="0" y="4" width="8" height="5" fill="#e0b54a"/><path d="M2 4V2.5a2 2 0 0 1 4 0V4" fill="none" stroke="#e0b54a" stroke-width="1.2"/></svg></a>
  <a class="abs login" style="left:587px;width:88px">Login for your<br>Quillbrook account
    <svg width="8" height="9" viewBox="0 0 8 9"><rect x="0" y="4" width="8" height="5" fill="#e0b54a"/><path d="M2 4V2.5a2 2 0 0 1 4 0V4" fill="none" stroke="#e0b54a" stroke-width="1.2"/></svg></a>
  <nav class="abs nav-band nav">
    <a class="active" href="#">Home</a>
    <a href="#" style="left:107px">About us</a>
    <a href="#" style="left:192px">Associate</a>
    <a href="#" style="left:424px">Services</a>
    <a href="#" style="left:508px">Our Mission</a>
    <a href="#" style="left:606px">Contact us</a>
  </nav>
  <div class="abs logo">VELMORFIELD<br>Financial</div>
  <div class="abs ribbon">
    <svg width="250" height="24" viewBox="0 0 250 24"><path d="M0 2H250L238 12L250 22H0L12 12Z" fill="#f1e4cb" stroke="#b7a784"/></svg>
    <span>"always do right. this gratify some people &amp; astonish the rest."</span>
  </div>
  <div class="abs call">
    <svg width="20" height="14" viewBox="0 0 20 14"><ellipse cx="10" cy="7" rx="10" ry="7" fill="#3fa34a"/><path d="M6 4c0 4 4 7 8 7l1-2-2-1-1 1c-1-.5-2.5-2-3-3l1-1-1-2z" fill="#fff"/></svg>Call us for free Consltation : 303-418-7639
  </div>
  <section class="abs slider">
    <div class="abs slide-img" role="img" aria-label="Photo of a hand dropping a coin into a white piggy bank on a sunny beach"></div>
    <h2 class="abs slide-title" style="font-weight:400">RETIREMENT PLAN</h2>
    <p class="abs slide-text">Lorem Ipsum is simply dummy text of the printing and typesetting industry. Lorem Ipsum has been the industry's standard dummy text ever since the 1500s, when an unknown printer took a galley of type and scrambled it to make a type specimen book. It has survived not only five centuries, but also the leap into electronic typesetting, remaining essentially unchanged. It was popularised in the 1960s with the release of Letraset sheets containing Lorem Ipsum passages, and more recently with desktop publish-</p>
    <a class="abs btn-light" style="left:471px;top:150px;width:61px;height:14px;line-height:12px">Learn more</a>
    <div class="abs dots"><i></i><i></i><i></i><i></i></div>
  </section>
</header>

<main>
  <article class="abs card" style="left:8px;top:365px">
    <h3>ABOUT US</h3>
    <div class="photo" role="img" aria-label="Photo of a businessman in a suit and glasses" style="background:linear-gradient(90deg,#c8ccd0,#6e7075 50%,#d4d6d8)"></div>
    <p>Lorem Ipsum is simply dummy text of the printing and typesetting industry. Lorem Ipsum has been the industry's standard dummy text ever since the 1500s, when an unknown printer took a galley of type and scrambled it to make a type specimen book. It has survived not only five</p>
    <a class="btn-dark more">Learn more</a>
  </article>
  <article class="abs card" style="left:220px;top:365px">
    <h3>WHY CUSTOMER CHOSE US</h3>
    <div class="photo" role="img" aria-label="Photo of a smiling business team" style="background:linear-gradient(90deg,#a9c4dc,#d8c9b8 50%,#7d8ea0)"></div>
    <p>Lorem Ipsum is simply dummy text of the printing and typesetting industry. Lorem Ipsum has been the industry's standard dummy text ever since the 1500s, when an unknown printer took a galley of type and scrambled it to make a type specimen book. It has survived not only five</p>
    <a class="btn-light more">Learn more</a>
  </article>
  <article class="abs card" style="left:8px;top:547px">
    <h3>OUR MISSION</h3>
    <div class="photo" role="img" aria-label="Photo of a smiling man in front of colleagues" style="background:linear-gradient(90deg,#b8cde0,#d9b89c 50%,#c7d6e3)"></div>
    <p>Lorem Ipsum is simply dummy text of the printing and typesetting industry. Lorem Ipsum has been the industry's standard dummy text ever since the 1500s, when an unknown printer took a galley of type and scrambled it to make a type specimen book. It has survived not only five</p>
    <a class="btn-light more">Learn more</a>
  </article>
  <article class="abs card" style="left:220px;top:547px">
    <h3>SUPPORT</h3>
    <div class="photo" role="img" aria-label="Photo of a smiling support agent" style="background:linear-gradient(90deg,#e6eef2,#d8bfa8 55%,#f1f3f4)"></div>
    <p>Lorem Ipsum is simply dummy text of the printing and typesetting industry. Lorem Ipsum has been the industry's standard dummy text ever since the 1500s, when an unknown printer took a galley of type and scrambled it to make a type specimen book. It has survived not only five</p>
    <a class="btn-light more">Learn more</a>
  </article>

  <form class="abs panel" style="left:435px;top:364px;width:241px;height:231px">
    <svg class="abs" style="left:15px;top:14px" width="30" height="14" viewBox="0 0 30 14"><rect x=".5" y=".5" width="29" height="13" fill="#d9cdb6" stroke="#a89a80"/><path d="M.5 .5L15 8 29.5 .5" fill="none" stroke="#a89a80"/></svg>
    <h4 style="left:60px;top:14px">CONTACT US</h4>
    <span class="label" style="top:50px">Name *</span><span class="field" style="top:45px"></span>
    <span class="label" style="top:75px">Last Name *</span><span class="field" style="top:70px"></span>
    <span class="label" style="top:100px">Email *</span><span class="field" style="top:95px"></span>
    <span class="label" style="top:124px">Comapny *</span><span class="field" style="top:119px"></span>
    <span class="label" style="top:147px">Message *</span><span class="field" style="top:144px;height:43px"></span>
    <a class="abs btn-dark" style="left:162px;top:205px;width:63px;height:14px;line-height:14px">Learn more</a>
  </form>
  <form class="abs panel" style="left:435px;top:610px;width:241px;height:94px">
    <h4 style="left:20px;top:11px">NEWSLETTER SIGN UP</h4>
    <div class="abs" style="left:14px;top:39px;width:210px;height:21px;background:#ddd0bb;font-size:9px;line-height:21px;padding-left:10px;color:#2b2b25">Enter your Email</div>
    <a class="abs btn-dark" style="left:149px;top:67px;width:76px;height:23px;line-height:23px;font-size:9px;font-weight:400">SIGN UP</a>
  </form>

  <div class="abs sep"></div>

  <section>
    <h4 class="abs sec-title" style="left:8px;font-weight:400">LATEST NEWS</h4>
    <svg class="abs" style="left:96px;top:759px" width="28" height="18" viewBox="0 0 28 18"><rect x="3" y="2" width="22" height="14" fill="#e9e6de" stroke="#8d8a80" transform="rotate(-12 14 9)"/><path d="M8 7h12M8 10h12M8 13h8" stroke="#8d8a80" transform="rotate(-12 14 9)"/></svg>
    <div class="abs date" style="top:787px"><b>28</b><span>Feb</span></div>
    <div class="abs blurb" style="left:54px;top:784px;width:103px">Lorem Ipsum is simply dummy text of the printing and typeset-ting industry. Lorem Ipsum has been the industry's standard</div>
    <a class="abs rm" style="left:115px;top:820px">Learn more</a>
    <div class="abs date" style="top:857px"><b>28</b><span>Feb</span></div>
    <div class="abs blurb" style="left:54px;top:855px;width:103px">Lorem Ipsum is simply dummy text of the printing and typeset-ting industry. Lorem Ipsum has been the industry's standard</div>
    <a class="abs rm" style="left:115px;top:890px">Learn more</a>
    <div class="abs date" style="top:928px"><b>28</b><span>Feb</span></div>
    <div class="abs blurb" style="left:54px;top:926px;width:103px">Lorem Ipsum is simply dummy text of the printing and typeset-ting industry. Lorem Ipsum has been the industry's standard</div>
    <a class="abs rm" style="left:115px;top:961px">Learn more</a>
  </section>
  <div class="abs vdiv" style="left:181px"></div>

  <section>
    <h4 class="abs sec-title" style="left:207px;font-weight:400">TESTIMONIALS</h4>
    <svg class="abs" style="left:292px;top:759px" width="26" height="20" viewBox="0 0 26 20"><rect x="2" y="2" width="20" height="16" fill="#f1efe8" stroke="#8d8a80"/><path d="M5 7h14M5 10h14M5 13h9" stroke="#8d8a80"/><path d="M16 17l8-10" stroke="#d8a43c" stroke-width="2"/></svg>
    <div class="abs blurb" style="left:207px;top:784px;width:149px">Lorem Ipsum is simply dummy text of the printing and typesetting industry. Lorem Ipsum has been the industry's standard dummy text ever since the 1500s, when an</div>
    <span class="abs" style="left:318px;top:820px;font-style:italic;font-size:6px">Mr Halden</span>
    <div class="abs hdiv" style="top:836px"></div>
    <div class="abs blurb" style="left:207px;top:854px;width:149px">Lorem Ipsum is simply dummy text of the printing and typesetting industry. Lorem Ipsum has been the industry's standard dummy text ever since the 1500s, when an</div>
    <span class="abs" style="left:318px;top:890px;font-style:italic;font-size:6px">Mr Halden</span>
    <div class="abs hdiv" style="top:907px"></div>
    <div class="abs blurb" style="left:207px;top:926px;width:149px">Lorem Ipsum is simply dummy text of the printing and typesetting industry. Lorem Ipsum has been the industry's standard dummy text ever since the 1500s, when an</div>
    <span class="abs" style="left:318px;top:962px;font-style:italic;font-size:6px">Mr Halden</span>
  </section>
  <div class="abs vdiv" style="left:385px"></div>

  <section>
    <h4 class="abs sec-title" style="left:418px;font-weight:400">LATEST EVENT</h4>
    <svg class="abs" style="left:509px;top:758px" width="19" height="19" viewBox="0 0 19 19"><rect x="1" y="3" width="17" height="15" fill="#f4f2ee" stroke="#8d8a80"/><rect x="1" y="3" width="17" height="4" fill="#c8413a"/><path d="M4 10h2M8.5 10h2M13 10h2M4 14h2M8.5 14h2M13 14h2" stroke="#8d8a80" stroke-width="1.5"/></svg>
    <div class="abs event-img" style="top:785px" role="img" aria-label="Photo of business people joining hands in a team huddle"></div>
    <div class="abs blurb" style="left:540px;top:788px;width:136px">Lorem Ipsum is simply dummy text of the printing and typesetting industry. Lorem Ipsum has been the industry's standard dummy text ever since the 1500s, when an</div>
    <a class="abs" style="left:543px;top:832px;text-decoration:underline;font-weight:700;font-size:6.5px">Read more</a>
    <span class="abs" style="left:628px;top:832px;font-size:6.5px">Feb -28-2013</span>
    <div class="abs event-img" style="top:850px" role="img" aria-label="Photo of business people joining hands in a team huddle"></div>
    <div class="abs blurb" style="left:540px;top:852px;width:136px">Lorem Ipsum is simply dummy text of the printing and typesetting industry. Lorem Ipsum has been the industry's standard dummy text ever since the 1500s, when an</div>
    <a class="abs" style="left:543px;top:895px;text-decoration:underline;font-weight:700;font-size:6.5px">Read more</a>
    <span class="abs" style="left:628px;top:895px;font-size:6.5px">Feb -28-2013</span>
    <div class="abs event-img" style="top:913px" role="img" aria-label="Photo of business people joining hands in a team huddle"></div>
    <div class="abs blurb" style="left:540px;top:915px;width:136px">Lorem Ipsum is simply dummy text of the printing and typesetting industry. Lorem Ipsum has been the industry's standard dummy text ever since the 1500s, when an</div>
    <a class="abs" style="left:543px;top:968px;text-decoration:underline;font-weight:700;font-size:6.5px">Read more</a>
    <span class="abs" style="left:628px;top:968px;font-size:6.5px">Feb -28-2013</span>
  </section>

  <div class="abs call-strip"></div>
  <div class="abs call-pill">
    <svg width="14" height="10" viewBox="0 0 14 10"><path d="M1 3c3-3 9-3 12 0l-1 2-3-1V3H5v1L2 5z" fill="#333"/><rect x="3" y="5" width="8" height="5" rx="1" fill="#333"/></svg>
    Call us now for Free Consultation
  </div>
</main>

<footer class="abs footer">
  <h5 style="left:8px">QUICK LINKS</h5>
  <ul style="left:8px"><li>Home</li><li>About us</li><li>Services</li><li>Associate</li><li>Our  mission</li><li>Contact us</li><li>Privacy policy</li><li>Terms of use</li><li>Site map</li></ul>
  <h5 style="left:182px">SERVICES</h5>
  <ul style="left:182px"><li>Services 1</li><li>Services 2</li><li>Services 3</li><li>Services 4</li><li>Services5</li><li>Services6</li><li>Services7</li></ul>
  <h5 style="left:355px">CONTACT US</h5>
  <div class="info" style="left:355px;top:30px;font-size:10px">Address :</div>
  <div class="info" style="left:355px;top:48px">Comapny Address Goes Herea:</div>
  <div class="info" style="left:355px;top:83px">Phone : 303-555-0148<br>Email : info@velmorfield.net</div>
  <h5 style="left:528px">SOCIAL MEDIA LINKS</h5>
  <span class="social" style="left:528px" aria-label="Social link"></span>
  <span class="social" style="left:568px" aria-label="Social link"></span>
  <span class="social" style="left:609px" aria-label="Social link"></span>
</footer>
<div class="abs brand"><i></i><b>VELMORFIELD</b><span>Financial Consultant</span></div>
<div class="abs copy">All Copyright reserved by comapny name</div>

</body>
</html>
```